Stationery design for software development / consultancy company

We need stationary design based on company logo.

We are based in London, UK and we are providing integration solutions development / consultancy services for VEQ integration projects across UK.

Our name refers two words - integration and grace - and it shows our clients our main specialization field and key characteristics of our solutions / products. We also would like to be associated with follow words: smart, reliable, unique.

Project delivery should include:
- Powerpoint template (needs to have a Cover Page, Table of Contents, 1-2 sample pages, and a Closing/Summary slide at the end)
- Letterhead A4 (Word template)
- Standard invoice A4 (Word template)
- With Compliments Slips A5 (Word template)
- Business card (adobe illustrator)

Attached is logo in vector (please use logo with white background!) and company details for printed stationery.

highly skilled IT professionals

Software

• Clear background in all A4/A5 documents.
All text should be editable, i.e. I will need sources.
• I would prefer light, web 2.0 style colours, follow are in my main interest:
- combination of light grey and orange
- Logo colours
• Please no watermarks on printed stationary

```html
<!DOCTYPE html>
<html lang="en">
<head>
<meta charset="utf-8">
<title>Brightmoor presentation template</title>
<link rel="stylesheet" href="https://fonts.googleapis.com/css2?family=Cabin:wght@400;600;700&display=swap">
<style>
  :root {
    --page-bg: #e6e6e6;
    --slide-white: #ffffff;
    --slide-mist: #ebebeb;
    --ink: #222222;
    --ink-soft: #333333;
    --brand-grey: #5a5a5a;
    --brand-orange: #f0931e;
    --band-dark: #2e2d2e;
    --band-light: #4a494a;
    --accent-green: #8cc63f;
    --accent-blue: #2a9fd8;
    --footer-text: #ffffff;
  }
  * { margin: 0; padding: 0; box-sizing: border-box; }
  html, body { width: 1200px; height: 808px; overflow: hidden; }
  body {
    background: var(--page-bg);
    font-family: "Cabin", "Gill Sans", sans-serif;
    color: var(--ink);
    position: relative;
  }
  .slide {
    position: absolute;
    width: 474px;
    height: 354px;
    background: radial-gradient(ellipse at 20% 30%, var(--slide-mist) 0%, var(--slide-white) 60%);
    box-shadow: 0 2px 6px rgba(0,0,0,0.25);
    overflow: hidden;
  }
  .slide--cover   { left: 111px; top: 28px; }
  .slide--first   { left: 615px; top: 28px; width: 472px; }
  .slide--second  { left: 111px; top: 421px; width: 471px; height: 352px; }
  .slide--closing { left: 616px; top: 421px; }
  .slide__band { position: absolute; left: 0; bottom: 0; width: 100%; height: 70px; }
  .slide__url {
    position: absolute; left: 28px; bottom: 12px;
    font-size: 6px; color: var(--footer-text); letter-spacing: 0.1px;
  }
  .slide__url b { font-weight: 700; }
  .brand {
    position: absolute; display: flex; align-items: center; gap: 7px;
    color: var(--brand-grey); font-weight: 600; letter-spacing: -0.2px;
  }
  .brand__dot { border-radius: 50%; background: var(--brand-orange); }
  .brand--large { right: 40px; top: 46px; font-size: 30px; }
  .brand--large .brand__dot { width: 24px; height: 24px; }
  .brand--small { right: 58px; top: 33px; font-size: 19px; }
  .brand--small .brand__dot { width: 15px; height: 15px; }
  .cover-title { position: absolute; right: 40px; top: 244px; text-align: right; }
  .cover-title h1 { font-size: 31px; font-weight: 700; color: var(--ink); line-height: 1; letter-spacing: -0.2px; }
  .cover-title p { font-size: 18.5px; color: var(--ink-soft); margin-top: 2px; }
  .content { position: absolute; left: 58px; top: 72px; width: 357px; }
  .content h2 { font-size: 20px; font-weight: 700; color: var(--brand-orange); margin-bottom: 5px; }
  .content p {
    font-size: 8.4px; line-height: 13.2px; text-align: justify; color: var(--ink);
    margin-bottom: 13px;
  }
  .closing-note { position: absolute; right: 37px; top: 207px; text-align: right; }
  .closing-note h1 { font-size: 31px; font-weight: 700; line-height: 1; color: var(--ink); letter-spacing: -0.2px; }
  .closing-note p { font-size: 18.5px; color: var(--ink-soft); margin-top: 1px; }
  .contact { position: absolute; right: 37px; top: 281px; text-align: right; font-size: 8.5px; color: var(--ink); line-height: 14px; }
  .contact strong { font-size: 12.5px; font-weight: 700; }
  .contact svg { vertical-align: -1px; margin-right: 3px; }
</style>
</head>
<body>

  <section class="slide slide--cover">
    <div class="brand brand--large"><span class="brand__dot"></span>Brightmoor</div>
    <div class="cover-title">
      <h1>Your Title Goes Here</h1>
      <p>Subtitle Goes Here</p>
    </div>
    <svg class="slide__band" viewBox="0 0 474 70" preserveAspectRatio="none">
      <defs>
        <linearGradient id="band-cover" x1="0" y1="0" x2="0" y2="1">
          <stop offset="0" stop-color="var(--band-light)"/>
          <stop offset="1" stop-color="var(--band-dark)"/>
        </linearGradient>
      </defs>
      <path d="M0,16 Q200,56 474,36 L474,70 L0,70 Z" fill="url(#band-cover)"/>
      <path d="M0,6 Q140,34 290,40" stroke="var(--accent-green)" stroke-width="3" fill="none"/>
      <path d="M290,40 Q400,40 474,32" stroke="var(--accent-blue)" stroke-width="3" fill="none"/>
    </svg>
    <div class="slide__url">www.<b>brightmoor</b>.co.uk</div>
  </section>

  <section class="slide slide--first">
    <div class="brand brand--small"><span class="brand__dot"></span>Brightmoor</div>
    <div class="content">
      <h2>Heading 1</h2>
      <p>Lorem Ipsum is simply dummy text of the printing and typesetting industry. Lorem Ipsum has been the industry's standard dummy text ever since the 1500s, when an unknown printer took a galley of type and scrambled it to make a type specimen book. It has survived not only five centuries, but also the leap into electronic typesetting, remaining essentially unchanged. It was popularised in the 1960s with the release of Letraset sheets containing Lorem Ipsum passages, and more recently with desktop publishing software like Aldus PageMaker including versions of Lorem Ipsum.</p>
      <p>Lorem Ipsum is simply dummy text of the printing and typesetting industry. Lorem Ipsum has been the industry's standard dummy text ever since the 1500s, when an unknown printer took a galley of type and scrambled it to make a type specimen book. It has survived not only five centuries, but also the leap into electronic typesetting, remaining essentially unchanged. It was popularised in the 1960s with the release of Letraset sheets containing Lorem Ipsum passages, and more recently with desktop publishing software like Aldus PageMaker including versions of Lorem Ipsum.</p>
    </div>
    <svg class="slide__band" viewBox="0 0 474 70" preserveAspectRatio="none">
      <path d="M0,16 Q200,56 474,36 L474,70 L0,70 Z" fill="var(--band-dark)"/>
      <path d="M0,6 Q140,34 290,40" stroke="var(--accent-green)" stroke-width="3" fill="none"/>
      <path d="M290,40 Q400,40 474,32" stroke="var(--accent-blue)" stroke-width="3" fill="none"/>
    </svg>
    <div class="slide__url">www.<b>brightmoor</b>.co.uk</div>
  </section>

  <section class="slide slide--second">
    <div class="brand brand--small"><span class="brand__dot"></span>Brightmoor</div>
    <div class="content">
      <h2>Heading 2</h2>
      <p>Lorem Ipsum is simply dummy text of the printing and typesetting industry. Lorem Ipsum has been the industry's standard dummy text ever since the 1500s, when an unknown printer took a galley of type and scrambled it to make a type specimen book. It has survived not only five centuries, but also the leap into electronic typesetting, remaining essentially unchanged. It was popularised in the 1960s with the release of Letraset sheets containing Lorem Ipsum passages, and more recently with desktop publishing software like Aldus PageMaker including versions of Lorem Ipsum.</p>
      <p>Lorem Ipsum is simply dummy text of the printing and typesetting industry. Lorem Ipsum has been the industry's standard dummy text ever since the 1500s, when an unknown printer took a galley of type and scrambled it to make a type specimen book. It has survived not only five centuries, but also the leap into electronic typesetting, remaining essentially unchanged. It was popularised in the 1960s with the release of Letraset sheets containing Lorem Ipsum passages, and more recently with desktop publishing software like Aldus PageMaker including versions of Lorem Ipsum.</p>
    </div>
    <svg class="slide__band" viewBox="0 0 474 70" preserveAspectRatio="none">
      <path d="M0,16 Q200,56 474,36 L474,70 L0,70 Z" fill="var(--band-dark)"/>
      <path d="M0,6 Q140,34 290,40" stroke="var(--accent-green)" stroke-width="3" fill="none"/>
      <path d="M290,40 Q400,40 474,32" stroke="var(--accent-blue)" stroke-width="3" fill="none"/>
    </svg>
    <div class="slide__url">www.<b>brightmoor</b>.co.uk</div>
  </section>

  <section class="slide slide--closing">
    <div class="brand brand--large"><span class="brand__dot"></span>Brightmoor</div>
    <div class="closing-note">
      <h1>Thank you very much</h1>
      <p>for your valuable time.</p>
    </div>
    <div class="contact">
      Contact us | <strong>Jane Roe</strong><br>
      <svg width="9" height="7" viewBox="0 0 9 7"><rect x="0.5" y="0.5" width="8" height="6" fill="none" stroke="var(--ink)"/><path d="M0.5,0.5 L4.5,4 L8.5,0.5" fill="none" stroke="var(--ink)"/></svg>jane@brightmoor.co.uk
    </div>
    <svg class="slide__band" viewBox="0 0 474 70" preserveAspectRatio="none">
      <path d="M0,16 Q200,56 474,36 L474,70 L0,70 Z" fill="var(--band-dark)"/>
      <path d="M0,6 Q140,34 290,40" stroke="var(--accent-green)" stroke-width="3" fill="none"/>
      <path d="M290,40 Q400,40 474,32" stroke="var(--accent-blue)" stroke-width="3" fill="none"/>
    </svg>
    <div class="slide__url">www.<b>brightmoor</b>.co.uk</div>
  </section>

</body>
</html>
```